KTW Structural Approval Partners Certifiers

Professional Construction Consultancy Company Business Card - must keep logo colours see images below - examples have been added from my last competition - please see them as examples only!

Target Market(s)

Home Builders

Industry/Entity Type

Construction

Contact Information for Business Card

See "must haves"

Font styles to use
Sans Serif

Colors
ffffff
add136
000000

Requirements
Must have
• Daniel Moravec
• Director
• Phone: 0431 758 219
• Address: 17 Corrigan St,
• Holloway Vale, SA, 5098
• Email: ktwapprovalpartners@mailbox-example.com
• Website: www.ktwapprovalpartners.example.au
• Facebook: KTW Structural Approval Partners
Nice to have
• Side 1: full logo
• Side 2: company details
Should not have
• hard to read
• must be clear and professional

```html
<!DOCTYPE html>
<html lang="en">
<head>
<meta charset="utf-8">
<title>KTW Structural Approval Partners – Business Card</title>
<link rel="stylesheet" href="https://fonts.googleapis.com/css2?family=Montserrat:wght@400;600;700&display=swap">
<style>
  :root {
    --green: #add136;
    --black: #000000;
    --white: #ffffff;
    --paper: #f2f1e7;
    --stage: #2b2b2b;
    --ink: #1a1a1a;
  }
  * { box-sizing: border-box; margin: 0; padding: 0; }
  html, body { width: 1200px; height: 786px; overflow: hidden; }
  body {
    background: var(--stage);
    font-family: "Montserrat", Arial, sans-serif;
    display: flex;
    align-items: center;
    justify-content: center;
    gap: 60px;
  }
  .card {
    position: relative;
    width: 520px;
    height: 298px;
    border-radius: 18px;
    overflow: hidden;
    box-shadow: 0 14px 34px rgba(0,0,0,.45);
  }

  /* Front */
  .card-front { background: var(--black); display: flex; align-items: center; justify-content: center; }
  .wordmark { color: var(--green); font-weight: 700; line-height: 1; }
  .card-front .wordmark-initials { font-size: 96px; letter-spacing: -2px; }
  .card-front .wordmark-lines { font-size: 21px; letter-spacing: 1px; text-transform: uppercase; margin-top: 10px; line-height: 1.15; }
  .card-front .wordmark-tag { font-size: 15px; letter-spacing: 7px; text-transform: uppercase; margin-top: 12px; }

  /* Back */
  .card-back { background: var(--paper); color: var(--ink); }
  .card-back .wordmark { position: absolute; left: 40px; top: 28px; }
  .card-back .wordmark-initials { font-size: 54px; letter-spacing: -1px; }
  .card-back .wordmark-lines { font-size: 12px; letter-spacing: .5px; text-transform: uppercase; margin-top: 5px; line-height: 1.15; }
  .card-back .wordmark-tag { font-size: 9px; letter-spacing: 4.5px; text-transform: uppercase; margin-top: 6px; }

  .contact-list { position: absolute; left: 40px; top: 150px; list-style: none; font-size: 10.5px; line-height: 1.75; }
  .contact-list li { display: flex; align-items: center; gap: 7px; }
  .contact-icon { width: 11px; height: 11px; flex: none; }
  .social-mark { width: 10px; height: 10px; background: var(--green); flex: none; }

  .person { position: absolute; right: 38px; top: 150px; text-align: right; }
  .person-name { font-weight: 700; font-size: 15px; text-transform: uppercase; letter-spacing: .5px; }
  .person-role { font-size: 11px; margin-top: 3px; }

  .address { position: absolute; right: 38px; bottom: 28px; text-align: right; font-size: 11px; line-height: 1.5; }

  .swoosh { position: absolute; left: 0; bottom: 0; width: 520px; height: 298px; }
</style>
</head>
<body>

  <section class="card card-front" aria-label="Card front">
    <div class="wordmark">
      <div class="wordmark-initials">KTW</div>
      <div class="wordmark-lines">Structural Approval Partners</div>
      <div class="wordmark-tag">Certifiers</div>
    </div>
  </section>

  <section class="card card-back" aria-label="Card back">
    <svg class="swoosh" viewBox="0 0 520 298" aria-hidden="true">
      <path d="M0 230 C 90 250, 200 270, 260 298 L 0 298 Z" fill="var(--black)"/>
      <path d="M0 222 C 95 240, 205 262, 272 298" fill="none" stroke="var(--green)" stroke-width="5"/>
    </svg>

    <div class="wordmark">
      <div class="wordmark-initials">KTW</div>
      <div class="wordmark-lines">Structural Approval Partners</div>
      <div class="wordmark-tag">Certifiers</div>
    </div>

    <ul class="contact-list">
      <li>
        <svg class="contact-icon" viewBox="0 0 24 24" aria-hidden="true"><path fill="var(--green)" d="M6.6 10.8a15 15 0 0 0 6.6 6.6l2.2-2.2a1 1 0 0 1 1-.25 11.4 11.4 0 0 0 3.6.57 1 1 0 0 1 1 1V20a1 1 0 0 1-1 1A17 17 0 0 1 3 4a1 1 0 0 1 1-1h3.5a1 1 0 0 1 1 1c0 1.25.2 2.45.57 3.57a1 1 0 0 1-.25 1z"/></svg>
        0431 758 219
      </li>
      <li>
        <svg class="contact-icon" viewBox="0 0 24 24" aria-hidden="true"><rect x="2" y="5" width="20" height="14" rx="2" fill="var(--green)"/><path d="M3 6l9 7 9-7" fill="none" stroke="var(--paper)" stroke-width="2"/></svg>
        ktwapprovalpartners@mailbox-example.com
      </li>
      <li>
        <svg class="contact-icon" viewBox="0 0 24 24" aria-hidden="true"><circle cx="12" cy="12" r="10" fill="var(--green)"/><path d="M2 12h20M12 2c3 3 3 17 0 20M12 2c-3 3-3 17 0 20" fill="none" stroke="var(--paper)" stroke-width="1.5"/></svg>
        www.ktwapprovalpartners.example.au
      </li>
      <li>
        <span class="social-mark" aria-hidden="true"></span>
        KTW Structural Approval Partners
      </li>
    </ul>

    <div class="person">
      <div class="person-name">Daniel Moravec</div>
      <div class="person-role">Director</div>
    </div>

    <address class="address" style="font-style: normal;">
      17 Corrigan St,<br>
      Holloway Vale,<br>
      SA, 5098
    </address>
  </section>

</body>
</html>
```